Need simple and modern looking business card with all my information on one side and logo on the other side
Info :
Company name - VELMAR CONSTRUCTION LLC
Company addres- 418 harbor 87th. Dunmoor park ny 10352
Email- velmarllc@tridomail.Com
Company phone number 555-318-6094
Cell number- 555-742-0583
Web site - velmarllc.Com
My name Gerald tomasino

Target Market(s)

Construction , home improvement, remodeling

Industry/Entity Type

Construction

Contact Information for Business Card

It has to be moder but at the same time simple

Font styles to use
Sans Serif

Colors
0255a3
ffffff
000000
f78f20
b1b1b1
9d9d9d
1b1b1b
33a6d7
ec1f27

Requirements
Must have
• My logo on one side maybe with a some kind of background on the other side all my information
Nice to have
• Some kind of background pictures provided by you .PLEASE HAVE ACCOUNT WITH PIXELVAULT WILL NOT PAY ANY EXTRA FEES .
Should not have
• Any kind of hamer, nails,screws, helmets itp. Please do not copy the other designs come up with something new.

```html
<!DOCTYPE html>
<html lang="en">
<head>
<meta charset="utf-8">
<title>Velmar Construction LLC – Business Card</title>
<link href="https://fonts.googleapis.com/css2?family=Lato:wght@400;700&display=swap" rel="stylesheet">
<style>
  :root {
    --stage: #e6e6e6;
    --card: #ffffff;
    --ink: #1b1b1b;
    --grey: #595959;
    --grey-light: #b1b1b1;
    --orange: #f78f20;
    --blue: #0255a3;
    --sky: #33a6d7;
    --red: #ec1f27;
  }
  * { box-sizing: border-box; margin: 0; padding: 0; }
  html, body { width: 1200px; height: 900px; overflow: hidden; }
  body {
    background: var(--stage);
    font-family: "Lato", Arial, sans-serif;
    position: relative;
  }
  .card {
    position: absolute;
    left: 250px;
    width: 700px;
    height: 400px;
    background: var(--card);
    box-shadow: 0 6px 18px rgba(0,0,0,0.18);
    overflow: hidden;
  }
  .card--back { top: 40px; }
  .card--front { top: 470px; }

  /* back side */
  .back-name {
    position: absolute;
    top: 40px;
    right: 44px;
    text-align: right;
    color: var(--ink);
    font-weight: 400;
    line-height: 1.05;
  }
  .back-name .wordmark { font-size: 34px; letter-spacing: 2px; }
  .back-name .descriptor { font-size: 13px; letter-spacing: 2px; }
  .skyline {
    position: absolute;
    left: 0;
    bottom: 0;
    width: 100%;
    height: 210px;
    background: linear-gradient(100deg, rgba(236,31,39,0.12) 0%, rgba(2,85,163,0.14) 40%, rgba(247,143,32,0.12) 70%, rgba(157,157,157,0.14) 100%);
  }

  /* front side */
  .contact {
    position: absolute;
    top: 38px;
    left: 44px;
    color: var(--grey);
    font-size: 16px;
    line-height: 1.25;
  }
  .contact .person { font-size: 20px; letter-spacing: 1px; color: var(--grey); }
  .contact .role { color: var(--orange); font-size: 15px; margin-bottom: 12px; }
  .contact .label { color: var(--orange); display: inline-block; width: 18px; }
  .contact .address { margin-top: 10px; }
  .contact .web { color: var(--orange); }

  .front-mark {
    position: absolute;
    right: 40px;
    bottom: 40px;
    display: flex;
    align-items: flex-end;
    gap: 16px;
    color: var(--ink);
    font-weight: 400;
  }
  .front-mark .square {
    width: 26px;
    height: 26px;
    background: var(--orange);
    margin-bottom: 14px;
  }
  .front-mark .name { text-align: right; line-height: 1; }
  .front-mark .wordmark { font-size: 96px; letter-spacing: 4px; }
  .front-mark .descriptor { font-size: 36px; letter-spacing: 4px; margin-top: 4px; }
</style>
</head>
<body>
  <section class="card card--back" aria-label="Card back">
    <div class="back-name">
      <div class="wordmark">VELMAR</div>
      <div class="descriptor">CONSTRUCTION LLC</div>
    </div>
    <div class="skyline" role="img" aria-label="Decorative skyline of outlined buildings in red, blue, orange and grey"></div>
  </section>

  <section class="card card--front" aria-label="Card front">
    <div class="contact">
      <div class="person">GERALD TOMASINO</div>
      <div class="role">managing director</div>
      <div><span class="label">P</span>555-318-6094</div>
      <div><span class="label">M</span>555-742-0583</div>
      <div><span class="label">E</span>velmarllc@tridomail.Com</div>
      <div class="address">418 harbor 87th. Dunmoor park ny 10352</div>
      <div class="web">www.velmarllc.com</div>
    </div>
    <div class="front-mark">
      <div class="square"></div>
      <div class="name">
        <div class="wordmark">VELMAR</div>
        <div class="descriptor">CONSTRUCTION LLC</div>
      </div>
    </div>
  </section>
</body>
</html>
```